Tamarack Hearth Partners Business Card

Looking for a new business card layout. We are a real estate firm w/ a logo, old design attached. Must keep the same elements on there, just need a fresh look and possible some foil accents. Looking for a simpler design w/ more modern style.

Target Market(s)

Real Estate clients

Industry/Entity Type

Real Estate Agent

Contact Information for Business Card

see attached

Font styles to use
Sans Serif

Requirements
Must have
• all elements on current biz card
Nice to have
• modern look, simpler than we have!
Should not have
• no serif fonts

```html
<!DOCTYPE html>
<html lang="en">
<head>
<meta charset="utf-8">
<title>Tamarack Hearth Partners – Business Card</title>
<link rel="stylesheet" href="https://fonts.googleapis.com/css2?family=Jura:wght@300;400&family=Questrial&family=Syncopate:wght@700&display=swap">
<style>
  :root {
    --backdrop: #cfc4c4;
    --card: #030303;
    --gold: #b98a36;
    --gold-light: #c9a04e;
    --white: #ffffff;
    --photo-top: #d8c8b4;
    --photo-bottom: #2fc3c4;
  }
  * { margin: 0; padding: 0; box-sizing: border-box; }
  html, body { width: 927px; height: 1200px; overflow: hidden; }
  body { background: var(--backdrop); position: relative; font-family: "Questrial", sans-serif; }

  .card {
    position: absolute;
    background: var(--card);
    box-shadow: 4px 7px 0 var(--gold);
  }
  .card--front { left: 146px; top: 179px; width: 635px; height: 363px; }
  .card--back  { left: 146px; top: 600px; width: 632px; height: 361px; }

  .abs { position: absolute; }
  .frame { position: absolute; overflow: visible; }

  .monogram {
    position: absolute;
    font-family: "Jura", sans-serif;
    font-weight: 400;
    color: var(--gold);
    text-align: center;
    letter-spacing: 4px;
  }
  .agent-name {
    font-family: "Jura", sans-serif;
    font-weight: 300;
    color: var(--gold-light);
    text-transform: uppercase;
    white-space: nowrap;
  }
  .agent-title {
    font-family: "Syncopate", sans-serif;
    font-weight: 700;
    color: var(--white);
    text-transform: uppercase;
    white-space: nowrap;
  }
  .firm-name {
    font-family: "Jura", sans-serif;
    font-weight: 400;
    color: var(--gold);
    text-transform: uppercase;
    text-align: center;
    white-space: nowrap;
  }

  /* front */
  .card--front .monogram { left: 260px; top: 48px; width: 124px; font-size: 30px; line-height: 40px; }
  .card--front .agent-name { left: 0; width: 635px; text-align: center; font-size: 44px; letter-spacing: 17px; line-height: 40px; }
  .card--front .agent-name--first { top: 111px; }
  .card--front .agent-name--last { top: 157px; }
  .card--front .agent-title { left: 0; width: 635px; top: 213px; text-align: center; font-size: 11px; letter-spacing: 2.5px; }
  .card--front .firm-name { left: 0; width: 635px; top: 290px; font-size: 13px; letter-spacing: 4px; line-height: 17px; }

  /* back */
  .card--back .monogram { left: 74px; top: 48px; width: 94px; font-size: 26px; line-height: 34px; }
  .photo {
    position: absolute; left: 82px; top: 92px; width: 95px; height: 151px;
    background: linear-gradient(180deg, var(--photo-top) 0%, #c9a889 55%, var(--photo-bottom) 100%);
  }
  .card--back .firm-name { left: 40px; width: 176px; top: 259px; font-size: 10.5px; letter-spacing: 2.6px; line-height: 13px; }
  .card--back .agent-name { right: 47px; top: 29px; font-size: 27px; letter-spacing: 10px; margin-right: -10px; }
  .card--back .agent-title { right: 47px; top: 64px; font-size: 11px; letter-spacing: 2.3px; margin-right: -2.3px; }

  .contact-label {
    position: absolute; right: 278px;
    font-size: 12px; letter-spacing: 2.5px; color: var(--gold); text-transform: uppercase;
  }
  .contact-value {
    position: absolute; right: 50px; text-align: right;
    color: var(--white); white-space: nowrap; letter-spacing: 2px;
  }
  .phone { font-size: 16px; letter-spacing: 3px; }
  .email { font-size: 14px; letter-spacing: 1.5px; }
  .address { font-size: 13px; line-height: 22px; letter-spacing: 2.5px; }
  .icon { position: absolute; }
  .website {
    position: absolute; left: 0; width: 632px; top: 320px; text-align: center;
    color: var(--white); font-size: 15px; letter-spacing: 1.5px; font-style: italic;
  }
</style>
</head>
<body>

<section class="card card--front" aria-label="Card front">
  <svg class="frame" width="635" height="363" viewBox="0 0 635 363" aria-hidden="true">
    <path d="M260 71 H165 V262 H477 V71 H384" fill="none" stroke="var(--gold)" stroke-width="5"/>
  </svg>
  <div class="monogram">MV</div>
  <div class="agent-name agent-name--first abs">Marla</div>
  <div class="agent-name agent-name--last abs">Vance</div>
  <div class="agent-title abs">Principal Broker</div>
  <div class="firm-name abs">Tamarack Hearth<br>Partners</div>
</section>

<section class="card card--back" aria-label="Card back">
  <svg class="frame" width="632" height="361" viewBox="0 0 632 361" aria-hidden="true">
    <path d="M76 66 H52 V254 M166 66 H206 V254" fill="none" stroke="var(--gold)" stroke-width="3"/>
  </svg>
  <div class="monogram">MV</div>
  <div class="photo" role="img" aria-label="Portrait photo of the agent"></div>
  <div class="firm-name abs">Tamarack Hearth<br>Partners</div>

  <div class="agent-name abs">Marla Vance</div>
  <div class="agent-title abs">Principal Broker</div>

  <div class="contact-label" style="top:110px">Office.</div>
  <div class="contact-value phone" style="top:107px">541.555.0142</div>
  <div class="contact-label" style="top:135px">Cell.</div>
  <div class="contact-value phone" style="top:132px">541.555.0187</div>

  <svg class="icon" style="left:326px;top:190px" width="19" height="15" viewBox="0 0 19 15" aria-hidden="true">
    <rect x="1" y="1" width="17" height="13" fill="none" stroke="var(--gold)" stroke-width="2"/>
    <path d="M1 1 L9.5 8 L18 1 M1 14 L7 7 M18 14 L12 7" fill="none" stroke="var(--gold)" stroke-width="1.6"/>
  </svg>
  <div class="contact-value email" style="top:188px">marla@tamarackhearth.com</div>

  <svg class="icon" style="left:328px;top:249px" width="16" height="22" viewBox="0 0 16 22" aria-hidden="true">
    <path d="M8 21 C3 14 1.5 11 1.5 8 A6.5 6.5 0 0 1 14.5 8 C14.5 11 13 14 8 21 Z" fill="none" stroke="var(--gold)" stroke-width="1.8"/>
    <circle cx="8" cy="8" r="2.3" fill="none" stroke="var(--gold)" stroke-width="1.6"/>
  </svg>
  <div class="contact-value address" style="top:239px">418 NW Juniper Ave.<br>Pinecrest, OR 97000</div>

  <div class="website">TamarackHearth-Homes.com</div>
</section>

</body>
</html>
```